Brava Stone Oven Kitchen (restaurant)

Restaurant with a cool vibe.
We need a refresh of existing site. Appealing to a hip crowd of 25 or older age bracket (mid price to high small town). Constant changes food and cocktail menu. A vibing atmosphere with jazz funk hip music.
Must be able to scale for any device… phone/mobile device super important.
Instagram: @Brava.Linwell
Website: bravalinwell.example

Target Market(s)

25-55 age group

Number of Pages Required

1 page

Font styles to use
Sans Serif

Requirements
Must have
• Simple to navigate. Simplicity is the key to all sophistication.

Links/Buttons
Menu
Gift Cards
Reservations
Take Out
Contact Us
Should not have
• Please, nothing generic looking… no cookie cutter look. Originality

```html
<!DOCTYPE html>
<html lang="en">
<head>
<meta charset="utf-8">
<title>Brava Stone Oven Kitchen</title>
<link href="https://fonts.googleapis.com/css2?family=Great+Vibes&family=Montserrat:wght@400;500;600;700&family=Open+Sans:wght@400;600&family=Oswald:wght@400;500&family=PT+Sans+Narrow:wght@400;700&family=Roboto:wght@400;500;700&display=swap" rel="stylesheet">
<style>
:root{
  --red:#e01b1b;
  --red-deep:#b01010;
  --black:#000;
  --wood:#141414;
  --wood-light:#1f1f1f;
  --white:#fff;
  --grey:#b9b9b9;
  --muted:#6d6d6d;
  --star:#f2b01e;
}
*{margin:0;padding:0;box-sizing:border-box}
html,body{width:1200px;height:4418px;overflow:hidden;background:var(--black)}
body{position:relative;font-family:"Open Sans",sans-serif;color:var(--white)}
.abs{position:absolute}
.center{text-align:center}

/* backgrounds */
.wood{background:linear-gradient(90deg,#0d0d0d 0%,#1c1c1c 25%,#121212 50%,#1e1e1e 75%,#0f0f0f 100%)}
.hero-bg{left:0;top:0;width:1200px;height:1330px}
.takeout-bg{left:0;top:2357px;width:1200px;height:1126px}

/* nav */
.logo{font-family:"Montserrat",sans-serif;font-weight:700;color:var(--white);text-align:center;line-height:1}
.logo .name{font-size:38px;letter-spacing:2px}
.logo .tag{font-size:13px;font-weight:500;letter-spacing:.3px;margin-top:3px}
.nav{top:30px;left:380px;display:flex;gap:0;font-family:"Oswald",sans-serif;font-size:12px;letter-spacing:.3px}
.nav a{color:var(--white);text-decoration:none;position:absolute;white-space:nowrap}
.nav a.active{color:var(--red)}
.nav a.active::after{content:"";position:absolute;left:-6px;right:-18px;top:35px;height:2px;background:var(--red)}

/* hero */
.welcome{left:130px;top:228px;font-family:"Great Vibes",cursive;font-size:44px;color:var(--white);letter-spacing:1px}
.hero-title{left:110px;top:276px;font-family:"Roboto",sans-serif;font-weight:700;font-size:60px;line-height:64px;text-align:center;width:370px}
.hero-title .red{color:var(--red)}
.divider{display:block}
.btn-pill{left:203px;top:439px;width:188px;height:44px;border-radius:22px;background:var(--red);font-family:"Montserrat",sans-serif;font-weight:600;font-size:15px;display:flex;align-items:center;justify-content:center}
.hero-photo{left:560px;top:165px;width:640px;height:470px;background:radial-gradient(ellipse at 45% 50%,#d9b57a 0%,#9a5b2a 35%,#5b6b3a 55%,#3a3a40 75%,rgba(0,0,0,0) 100%);clip-path:polygon(4% 28%,12% 12%,30% 6%,55% 2%,80% 0,100% 4%,100% 74%,86% 86%,64% 98%,40% 92%,20% 80%,6% 62%,0 45%)}

/* section titles */
.sec-title{font-family:"PT Sans Narrow",sans-serif;font-weight:700;font-size:40px;text-align:center;line-height:1}
.sec-title .red{color:var(--red)}
.menu-title{font-family:"Roboto",sans-serif;font-weight:500;font-size:37px}

/* menu grid */
.tile{position:absolute;width:307px;height:224px;overflow:hidden}
.tile .ph{position:absolute;inset:0}
.tile .label{position:absolute;left:16px;right:16px;top:178px;height:34px;background:rgba(60,60,60,.75);border:1px solid rgba(255,255,255,.6);font-family:"Montserrat",sans-serif;font-weight:600;font-size:15px;letter-spacing:1.5px;display:flex;align-items:center;justify-content:center}
.tile .label.on{background:var(--red);border-color:var(--red)}

/* reservation */
.res-photo{left:0;top:1389px;width:600px;height:505px;background:linear-gradient(135deg,#6b4a2e 0%,#3d3a36 40%,#8a6a4a 70%,#c46a1a 100%);clip-path:polygon(0 5%,12% 4%,30% 0,55% 3%,72% 1%,86% 10%,100% 30%,97% 55%,86% 72%,70% 80%,52% 100%,30% 96%,12% 92%,0 88%)}
.body-copy{font-family:"Open Sans",sans-serif;font-size:17px;line-height:25px;color:#e9e9e9;text-align:center}
.btn-box{background:var(--red);font-family:"PT Sans Narrow",sans-serif;font-weight:700;font-size:19px;display:flex;align-items:center;justify-content:center}

/* gift cards */
.gift{position:absolute;width:308px;height:308px;border-radius:50%;background:#050505;box-shadow:0 0 34px 10px rgba(200,20,20,.55),inset 0 0 40px rgba(120,0,0,.5)}
.gift .voucher{position:absolute;left:51px;top:66px;width:206px;height:101px}
.gift h3{position:absolute;top:187px;width:100%;text-align:center;font-family:"PT Sans Narrow",sans-serif;font-weight:700;font-size:17px}
.gift p{position:absolute;top:210px;left:44px;right:44px;text-align:center;font-size:10.5px;line-height:15px;color:#c9c9c9}
.dots span{position:absolute;top:2356px;height:2px;width:50px}

/* take out photos */
.snap{position:absolute;border-radius:6px}

/* testimonials */
.card{position:absolute;width:297px;height:261px;background:linear-gradient(180deg,#0a0a0a 0%,#1a1111 100%);border:1px solid #3a1010;box-shadow:0 0 18px rgba(150,0,0,.35)}
.card .q{position:absolute;left:36px;top:20px;font-family:"Montserrat",sans-serif;font-weight:700;font-size:46px;color:var(--red);line-height:1}
.card h4{position:absolute;left:38px;top:70px;font-family:"Montserrat",sans-serif;font-weight:700;font-size:19px}
.card p{position:absolute;left:38px;right:24px;top:98px;font-family:"Montserrat",sans-serif;font-size:11px;line-height:19px;color:#d6d6d6}
.card .who{position:absolute;left:38px;top:186px;font-family:"Montserrat",sans-serif;font-size:11px;color:var(--muted)}
.card .stars{position:absolute;left:38px;top:203px;font-size:14px;color:var(--star);letter-spacing:1px}
.arrow{position:absolute}

/* contact */
.contact-panel{left:0;top:3483px;width:1200px;height:557px;background:linear-gradient(90deg,#000 35%,#3a0505 65%,#9a1208 100%)}
.contact-photo{left:0;top:3483px;width:662px;height:557px;background:linear-gradient(160deg,#8aa3c0 0%,#a9b9c8 20%,#8a5a40 40%,#6d4030 70%,#4c4a48 100%);clip-path:polygon(0 0,100% 0,79% 55%,100% 100%,0 100%)}
.contact-title{left:715px;top:3602px;font-family:"PT Sans Narrow",sans-serif;font-weight:700;font-size:36px}
.contact-lines{left:716px;font-family:"Roboto",sans-serif;font-weight:400;font-size:18px;line-height:27px;color:#f1f1f1}
.btn-outline{left:722px;top:3877px;width:172px;height:46px;border:2px solid var(--white);font-family:"Montserrat",sans-serif;font-weight:700;font-size:15px;display:flex;align-items:center;justify-content:center}
.to-top{left:1059px;top:4019px;width:42px;height:42px;border-radius:50%;background:var(--red);display:flex;align-items:center;justify-content:center}

/* footer */
.foot-h{font-family:"Montserrat",sans-serif;font-weight:700;font-size:14px;letter-spacing:.3px}
.foot-list{font-family:"Montserrat",sans-serif;font-size:12.5px;line-height:24px;color:#cfcfcf;list-style:none}
.social{position:absolute;top:4193px;width:38px;height:38px;border-radius:50%;background:var(--red);border:2px solid var(--white)}
.contact-row{display:flex;align-items:center;gap:10px;font-family:"Montserrat",sans-serif;font-size:10px;color:#cfcfcf;height:26px}
.rule{left:0;top:4337px;width:1200px;height:1px;background:#2a2a2a}
.legal{top:4366px;font-family:"Montserrat",sans-serif;font-size:11.5px;color:#bdbdbd}
</style>
</head>
<body>

<!-- HERO -->
<div class="abs wood hero-bg"></div>
<div class="abs logo" style="left:104px;top:16px;width:172px">
  <div class="name">BRAVA</div>
  <div class="tag">Stone Oven Kitchen</div>
</div>
<nav class="abs nav">
  <a class="active" style="left:12px">HOME</a>
  <a style="left:101px">ABOUT US</a>
  <a style="left:213px">MENU</a>
  <a style="left:303px">RESERVATION</a>
  <a style="left:432px">TAKEOUT</a>
  <a style="left:538px">GIFT CARDS</a>
  <a style="left:659px">CONTACT</a>
</nav>
<div class="abs hero-photo" role="img" aria-label="Close-up of stone-oven tacos with grilled meat, red cabbage and onion"></div>
<div class="abs welcome">Welcome to Brava</div>
<h1 class="abs hero-title">STONE OVEN<br><span class="red">KITCHEN</span></h1>
<svg class="abs divider" style="left:180px;top:398px" width="230" height="16" viewBox="0 0 230 16">
  <line x1="0" y1="8" x2="98" y2="8" stroke="#e01b1b" stroke-width="1.5"/>
  <line x1="132" y1="8" x2="230" y2="8" stroke="#e01b1b" stroke-width="1.5"/>
  <rect x="109" y="2" width="12" height="12" transform="rotate(45 115 8)" fill="#e01b1b"/>
</svg>
<div class="abs btn-pill">RESERVATION</div>

<!-- MENU -->
<h2 class="abs sec-title menu-title" style="left:0;width:1200px;top:702px">OUR <span class="red">MENU</span></h2>
<svg class="abs" style="left:508px;top:752px" width="184" height="16" viewBox="0 0 184 16">
  <line x1="0" y1="8" x2="76" y2="8" stroke="#fff" stroke-width="1.5"/>
  <line x1="108" y1="8" x2="184" y2="8" stroke="#fff" stroke-width="1.5"/>
  <rect x="86" y="2" width="12" height="12" transform="rotate(45 92 8)" fill="#fff"/>
</svg>

<div class="tile" style="left:122px;top:799px"><div class="ph" role="img" aria-label="Grilled burger platter with greens" style="background:linear-gradient(135deg,#d8d0c0,#6a7a3a 55%,#c4502a)"></div><div class="label on">BURGER</div></div>
<div class="tile" style="left:454px;top:799px"><div class="ph" role="img" aria-label="Toasted sandwich with meat and greens" style="background:linear-gradient(160deg,#c88a4a,#8a5a3a 45%,#4a6a2a)"></div><div class="label">SANDWICH</div></div>
<div class="tile" style="left:787px;top:799px"><div class="ph" role="img" aria-label="Stone-baked pizza on a wooden board" style="background:linear-gradient(135deg,#d8b070,#b04a2a 50%,#6a4a30)"></div><div class="label">SANDWICH</div></div>
<div class="tile" style="left:122px;top:1046px"><div class="ph" role="img" aria-label="Bowls of dips and spreads on a table" style="background:linear-gradient(135deg,#6a6a5a,#8a8a3a 40%,#c07030 75%,#3a2a20)"></div><div class="label">BURGER</div></div>
<div class="tile" style="left:454px;top:1046px"><div class="ph" role="img" aria-label="Tacos with cabbage and herbs" style="background:linear-gradient(150deg,#7a5a3a,#c0b080 40%,#8a3a7a 70%,#5a7a3a)"></div><div class="label">SANDWICH</div></div>
<div class="tile" style="left:787px;top:1046px"><div class="ph" role="img" aria-label="Roasted pork loin on a plate" style="background:linear-gradient(135deg,#4a4a3a,#c0a070 45%,#e8e0d0 80%)"></div><div class="label">SANDWICH</div></div>

<!-- RESERVATION -->
<div class="abs res-photo" role="img" aria-label="Restaurant interior with wooden bar and counter"></div>
<h2 class="abs sec-title" style="left:640px;width:450px;top:1466px">BOOK RESERVATION</h2>
<svg class="abs" style="left:772px;top:1518px" width="184" height="16" viewBox="0 0 184 16">
  <line x1="0" y1="8" x2="76" y2="8" stroke="#fff" stroke-width="1.5"/>
  <line x1="108" y1="8" x2="184" y2="8" stroke="#fff" stroke-width="1.5"/>
  <rect x="86" y="2" width="12" height="12" transform="rotate(45 92 8)" fill="#fff"/>
</svg>
<p class="abs body-copy" style="left:630px;width:470px;top:1551px">Lorem Ipsum is simply dummy text of the printing and typesetting industry. Lorem Ipsum has been the industry's standard dummy text ever since the 1500s.</p>
<p class="abs body-copy" style="left:630px;width:470px;top:1637px">when an unknown printer took a galley of type and scrambled it to make a type specimen book.</p>
<div class="abs btn-box" style="left:773px;top:1714px;width:182px;height:46px">BOOK NOW</div>

<!-- GIFT CARDS -->
<h2 class="abs sec-title" style="left:0;width:1200px;top:1906px">GIFT CARDS</h2>
<svg class="abs" style="left:508px;top:1956px" width="184" height="16" viewBox="0 0 184 16">
  <line x1="0" y1="8" x2="76" y2="8" stroke="#e01b1b" stroke-width="1.5"/>
  <line x1="108" y1="8" x2="184" y2="8" stroke="#e01b1b" stroke-width="1.5"/>
  <rect x="86" y="2" width="12" height="12" transform="rotate(45 92 8)" fill="#e01b1b"/>
</svg>
<div class="gift" style="left:134px;top:2011px">
  <div class="voucher" role="img" aria-label="Gold gift voucher with ribbon" style="background:linear-gradient(135deg,#f0d890,#c89a30 50%,#f4e4b0)"></div>
  <h3>GIFT CARD VOUCHER</h3>
  <p>Lorem Ipsum is simply dummy text of the printing and typesetting industry.</p>
</div>
<div class="gift" style="left:446px;top:2011px">
  <div class="voucher" role="img" aria-label="Red gift voucher with ribbon" style="background:linear-gradient(135deg,#e02020,#8a0808 55%,#c01010)"></div>
  <h3>GIFT CARD VOUCHER</h3>
  <p>Lorem Ipsum is simply dummy text of the printing and typesetting industry.</p>
</div>
<div class="gift" style="left:767px;top:2011px">
  <div class="voucher" role="img" aria-label="Sparkling red gift card with gold bow" style="background:linear-gradient(135deg,#d81840,#f0d0a0 45%,#c01030)"></div>
  <h3>GIFT CARD VOUCHER</h3>
  <p>Lorem Ipsum is simply dummy text of the printing and typesetting industry.</p>
</div>
<div class="dots"><span style="left:548px;background:#666"></span><span style="left:610px;background:#fff"></span></div>

<!-- TAKE OUT -->
<div class="abs wood takeout-bg"></div>
<h2 class="abs sec-title" style="left:138px;width:400px;top:2546px">TAKE OUT</h2>
<svg class="abs" style="left:256px;top:2598px" width="184" height="16" viewBox="0 0 184 16">
  <line x1="0" y1="8" x2="76" y2="8" stroke="#fff" stroke-width="1.5"/>
  <line x1="108" y1="8" x2="184" y2="8" stroke="#fff" stroke-width="1.5"/>
  <rect x="86" y="2" width="12" height="12" transform="rotate(45 92 8)" fill="#fff"/>
</svg>
<p class="abs body-copy" style="left:118px;width:460px;top:2631px">Lorem Ipsum is simply dummy text of the printing and typesetting industry. Lorem Ipsum has been the industry's standard dummy text ever since the 1500s.</p>
<p class="abs body-copy" style="left:118px;width:460px;top:2717px">when an unknown printer took a galley</p>
<div class="abs btn-box" style="left:257px;top:2781px;width:182px;height:45px">BOOK NOW</div>
<div class="snap" role="img" aria-label="Restaurant counter and dining room" style="left:617px;top:2458px;width:209px;height:206px;background:linear-gradient(140deg,#8a9aa8,#6a5040 50%,#3a3028)"></div>
<div class="snap" role="img" aria-label="Restaurant team together at the counter" style="left:617px;top:2684px;width:209px;height:206px;background:linear-gradient(160deg,#4a4a50,#7a6050 55%,#2a2a2a)"></div>
<div class="snap" role="img" aria-label="Colourful painted wall mural on the patio" style="left:843px;top:2571px;width:225px;height:247px;background:linear-gradient(170deg,#e06040,#d83030 35%,#7aa0c0 60%,#8a6a5a)"></div>

<!-- TESTIMONIALS -->
<h2 class="abs sec-title" style="left:0;width:1200px;top:3010px">TESTIMONIALS</h2>
<svg class="abs" style="left:508px;top:3060px" width="184" height="16" viewBox="0 0 184 16">
  <line x1="0" y1="8" x2="76" y2="8" stroke="#e01b1b" stroke-width="1.5"/>
  <line x1="108" y1="8" x2="184" y2="8" stroke="#e01b1b" stroke-width="1.5"/>
  <rect x="86" y="2" width="12" height="12" transform="rotate(45 92 8)" fill="#e01b1b"/>
</svg>
<svg class="arrow" style="left:80px;top:3220px" width="22" height="36" viewBox="0 0 22 36"><polyline points="18,3 4,18 18,33" fill="none" stroke="#fff" stroke-width="3"/></svg>
<svg class="arrow" style="left:1097px;top:3220px" width="22" height="36" viewBox="0 0 22 36"><polyline points="4,3 18,18 4,33" fill="none" stroke="#fff" stroke-width="3"/></svg>

<div class="card" style="left:129px;top:3111px">
  <div class="q">&ldquo;</div><h4>It Really tasty!</h4>
  <p>Lorem Ipsum is simply dummy text of the printing and typesetting industry. Lorem Ipsum has been the industry's standard dummy text ever since</p>
  <div class="who">Mara Quill</div><div class="stars">&#9733;&#9733;&#9733;&#9733;&#9733;</div>
</div>
<div class="card" style="left:453px;top:3111px">
  <div class="q">&ldquo;</div><h4>It Really tasty!</h4>
  <p>Lorem Ipsum is simply dummy text of the printing and typesetting industry. Lorem Ipsum has been the industry's standard dummy text ever since</p>
  <div class="who">Mara Quill</div><div class="stars">&#9733;&#9733;&#9733;&#9733;&#9733;</div>
</div>
<div class="card" style="left:773px;top:3111px">
  <div class="q">&ldquo;</div><h4>It Really tasty!</h4>
  <p>Lorem Ipsum is simply dummy text of the printing and typesetting industry. Lorem Ipsum has been the industry's standard dummy text ever since</p>
  <div class="who">Mara Quill</div><div class="stars">&#9733;&#9733;&#9733;&#9733;&#9733;</div>
</div>

<!-- CONTACT -->
<div class="abs contact-panel"></div>
<div class="abs contact-photo" role="img" aria-label="Brick restaurant building exterior on a street corner"></div>
<h2 class="abs contact-title">CONTACT US</h2>
<div class="abs contact-lines" style="top:3666px">48 Orchard Lane, Linwell, TX 10024<br>(555) 014-2252</div>
<div class="abs contact-lines" style="top:3742px">Monday to Thursday – 10pm till late<br>Friday and Saturday – 12pm till midnight<br>Sun – 12pm till 10pm<br>Public Holidays – Closed</div>
<div class="abs btn-outline">BOOK NOW</div>
<div class="abs to-top"><svg width="16" height="18" viewBox="0 0 16 18"><polyline points="2,8 8,2 14,8" fill="none" stroke="#fff" stroke-width="2"/><line x1="8" y1="2" x2="8" y2="17" stroke="#fff" stroke-width="2"/></svg></div>

<!-- FOOTER -->
<div class="abs logo" style="left:150px;top:4106px;width:182px">
  <div class="name">BRAVA</div>
  <div class="tag">Stone Oven Kitchen</div>
</div>
<div class="social" style="left:176px" role="img" aria-label="Social profile link"></div>
<div class="social" style="left:222px" role="img" aria-label="Social profile link"></div>
<div class="social" style="left:268px" role="img" aria-label="Social profile @Brava.Linwell"></div>

<div class="abs" style="left:413px;top:4106px">
  <div class="foot-h">NAVIGATION</div>
  <svg width="60" height="10" viewBox="0 0 60 10" style="display:block;margin:6px 0 10px"><line x1="0" y1="5" x2="22" y2="5" stroke="#e01b1b"/><line x1="38" y1="5" x2="60" y2="5" stroke="#e01b1b"/><rect x="26" y="1" width="8" height="8" transform="rotate(45 30 5)" fill="#e01b1b"/></svg>
  <ul class="foot-list"><li>Our Menu</li><li>Gift Cards</li><li>Reservation</li><li>Takeout</li><li>Contact Us</li></ul>
</div>
<div class="abs" style="left:605px;top:4106px">
  <div class="foot-h">WORKING HOURS</div>
  <svg width="60" height="10" viewBox="0 0 60 10" style="display:block;margin:6px 0 10px"><line x1="0" y1="5" x2="22" y2="5" stroke="#e01b1b"/><line x1="38" y1="5" x2="60" y2="5" stroke="#e01b1b"/><rect x="26" y="1" width="8" height="8" transform="rotate(45 30 5)" fill="#e01b1b"/></svg>
  <ul class="foot-list"><li>Thursday, July 1st -&nbsp; Open</li><li>Friday, July 2nd -&nbsp; Open</li><li>Saturday, July 3rd -&nbsp; Open</li><li>Sunday, July 4th -&nbsp; Closed</li></ul>
</div>
<div class="abs" style="left:854px;top:4106px">
  <div class="foot-h">CONTACT US</div>
  <svg width="60" height="10" viewBox="0 0 60 10" style="display:block;margin:6px 0 8px"><line x1="0" y1="5" x2="22" y2="5" stroke="#e01b1b"/><line x1="38" y1="5" x2="60" y2="5" stroke="#e01b1b"/><rect x="26" y="1" width="8" height="8" transform="rotate(45 30 5)" fill="#e01b1b"/></svg>
  <div class="foot-list" style="font-size:10px;font-weight:700;line-height:16px">BRAVA</div>
  <div class="contact-row"><svg width="12" height="14" viewBox="0 0 12 14"><path d="M6 1a4.5 4.5 0 0 0-4.5 4.5C1.5 9 6 13 6 13s4.5-4 4.5-7.5A4.5 4.5 0 0 0 6 1z" fill="#e01b1b"/><circle cx="6" cy="5.5" r="1.6" fill="#000"/></svg>12 Mercer Street | Linwell | L1N 2W4</div>
  <div class="contact-row"><svg width="12" height="12" viewBox="0 0 12 12"><path d="M2.5 1l2 2.5-1.2 1.5a7 7 0 0 0 3.7 3.7l1.5-1.2 2.5 2-1.2 1.5C5 11 1 7 1 2.2z" fill="#e01b1b"/></svg>Phone: 555-013-0765</div>
  <div class="contact-row"><svg width="13" height="10" viewBox="0 0 13 10"><rect x="0.5" y="0.5" width="12" height="9" fill="none" stroke="#e01b1b"/><polyline points="0.5,0.5 6.5,5.5 12.5,0.5" fill="none" stroke="#e01b1b"/></svg>Email: hello@bravalinwell.example</div>
</div>

<div class="abs rule"></div>
<div class="abs legal" style="left:167px">Copyright © 2021 Brava All Right Reserved</div>
<div class="abs legal" style="left:760px">Contact Us</div>
<div class="abs legal" style="left:853px">Terms &amp; Conditions</div>
<div class="abs legal" style="left:994px">Privacy Policy</div>

</body>
</html>
```